Garden Planting Plan Design Project

We sell DIY designer garden makeover kits, consisting of living plants and how-to planting plans in different styles, e.g. Tropical or Mediterranean gardens.
We need a design template for the how-to planting plan, which will then be laid out with each garden's kits content.
The winning designer will be hired to complete 6 design plans in total.
Idea sketches and concepts, rather than finished pieces, are welcome at this stage.
This document, the "Fernwick Plotcraft Manual", needs to embody our brand and present the information in an original, slick, contemporary and cool way.
The document will be available to customers as a download PDF, and as a printed piece (on recycled stock). For the downloadable, people will print it on their home printers, so this must be taken into consideration in the design (i.e. avoiding background colours or large photos which wont look good on low-quality printers). We dont think this will constrain you though.
The document should have 6-8 pages - we dont mind 'white space' and can see interesting possibilities for die cuts, use of the fold, and infographics.
The key is to use our great content in the most beautiful way possible. It's all about getting the customer excited about the design possibilities of their garden kit - we want them to be so delighted with the document that they put it on their "inspiration" pinboard.
If you need more direction, we will feedback asap.
Updates
Here is an example of a garden design plan which might spark your ideas.
Please note we are looking for concepts for this comp. Not expecting finished pieces. We are looking to work with a great designer who gets our brand and audience.
Re ICONS. If you are using, they should be:
? Sun,
? Part Shade
? Shade
? Garden Bed
? Pot
? Flower
Thanks all!!
Target Market(s)
Design-conscious urban professionals (male and female), decorators/DIYers, inexperienced gardeners (got to be easy to follow).
Requirements
Must have
- Content, more notes and examples of documents designs we like are in the Brief folder.
Should not have
- NO stock imagery please.

```html
<!DOCTYPE html>
<html lang="en">
<head>
<meta charset="utf-8">
<title>Fernwick Plotcraft Manual – Tropical Shade Garden Design Palette</title>
<link rel="stylesheet" href="https://fonts.googleapis.com/css2?family=Comfortaa:wght@700&family=Arimo:wght@400;700&display=swap">
<style>
  :root {
    --backdrop: #33462c;
    --paper: #ffffff;
    --brand-green: #8dc63f;
    --ink: #111111;
    --rust-red: #8b4337;
    --dark-green: #134523;
    --lime-leaf: #92c83e;
    --dappled-yellow: #dcbf26;
    --mid-green: #4c9e48;
    --hot-pink: #ec008c;
    --dark-red: #ab2933;
    --lime-paint: #b5d334;
    --pale-grey: #d2d3d5;
  }
  * { box-sizing: border-box; margin: 0; padding: 0; }
  html, body { width: 1200px; height: 900px; overflow: hidden; }
  body { background: var(--backdrop); position: relative; font-family: "Arimo", Arial, sans-serif; color: var(--ink); }

  .page {
    position: absolute; left: 301px; top: 28px; width: 598px; height: 843px;
    background: var(--paper); overflow: hidden;
  }
  .page-title {
    position: absolute; left: 95px; top: 117px;
    font-family: "Comfortaa", "Trebuchet MS", sans-serif; font-weight: 700;
    font-size: 29px; line-height: 42px; color: var(--brand-green); letter-spacing: 0.3px;
  }
  .palette-item { position: absolute; left: 98px; width: 420px; }
  .palette-label {
    position: relative; padding-left: 15px; font-size: 11px; line-height: 16px;
  }
  .palette-label::before {
    content: ""; position: absolute; left: 2px; top: 6px; width: 4px; height: 4px;
    border-radius: 50%; background: var(--brand-green);
  }
  .palette-label strong { font-weight: 700; }
  .swatch-row { position: absolute; left: 3px; display: flex; gap: 12px; }
  .swatch {
    width: 60px; height: 60px; border: 1.5px solid var(--brand-green);
    border-radius: 5px 24px 5px 24px;
    box-shadow: 3px 3px 3px rgba(0,0,0,0.45);
  }
  .swatch--rust { background: var(--rust-red); }
  .swatch--dark-green { background: var(--dark-green); }
  .swatch--lime-leaf { background: var(--lime-leaf); }
  .swatch--yellow { background: var(--dappled-yellow); }
  .swatch--mid-green { background: var(--mid-green); }
  .swatch--pink { background: var(--hot-pink); }
  .swatch--dark-red { background: var(--dark-red); }
  .swatch--lime-paint { background: var(--lime-paint); }
  .swatch--grey { background: var(--pale-grey); }
  .swatch--bark { background: radial-gradient(circle at 40% 40%, #7a4a2c, #4a2a18); }
  .swatch--pebbles { background: radial-gradient(circle at 50% 50%, #d9cdb8, #a89a84); }
  .swatch--grass { background: linear-gradient(160deg, #2f6a3a, #173a22); }
  .swatch--lomandra { background: linear-gradient(160deg, #c6d85a, #7fa12e); }
  .swatch--lillypilly { background: radial-gradient(circle at 50% 45%, #5f9a4a, #1f3f1c); }

  .footer-brand {
    position: absolute; left: 45px; top: 794px;
    font-size: 13px; font-weight: 700; color: var(--brand-green); letter-spacing: -0.2px;
    display: flex; align-items: center; gap: 5px;
  }
  .footer-brand .brand-dot { width: 9px; height: 9px; border-radius: 50%; background: var(--brand-green); }
  .footer-kit {
    position: absolute; left: 183px; top: 796px;
    font-family: "Comfortaa", "Trebuchet MS", sans-serif; font-weight: 700;
    font-size: 11.5px; letter-spacing: 2.2px; color: var(--brand-green);
  }
  .corner-frame { position: absolute; right: 0; bottom: 0; }
  .page-number { position: absolute; left: 565px; top: 807px; font-size: 12px; }
</style>
</head>
<body>
  <main class="page">
    <h1 class="page-title">Design palette for the<br>Tropical Shade Garden</h1>

    <section class="palette-item" style="top:207px">
      <p class="palette-label"><strong>Plant colours</strong> - Rust red, dark green, dappled yellow, white and green</p>
      <div class="swatch-row" style="top:33px">
        <div class="swatch swatch--rust"></div>
        <div class="swatch swatch--dark-green"></div>
        <div class="swatch swatch--lime-leaf"></div>
        <div class="swatch swatch--yellow"></div>
        <div class="swatch swatch--mid-green"></div>
      </div>
    </section>

    <section class="palette-item" style="top:317px">
      <p class="palette-label"><strong>Complementary paint and pot colours</strong> - Hot pink, dark red, lime green,<br>pale grey</p>
      <div class="swatch-row" style="top:40px">
        <div class="swatch swatch--pink"></div>
        <div class="swatch swatch--dark-red"></div>
        <div class="swatch swatch--lime-paint"></div>
        <div class="swatch swatch--grey"></div>
      </div>
    </section>

    <section class="palette-item" style="top:428px">
      <p class="palette-label"><strong>Mulch</strong> - Small cream river pebbles, dark brown small chip pine bark</p>
      <div class="swatch-row" style="top:22px">
        <div class="swatch swatch--bark" role="img" aria-label="Dark brown small chip pine bark mulch"></div>
        <div class="swatch swatch--pebbles" role="img" aria-label="Small cream river pebbles"></div>
      </div>
    </section>

    <section class="palette-item" style="top:520px">
      <p class="palette-label"><strong>Complementary border plantings</strong> - native grasses, Lomandra, Lillypilly for<br>hedge</p>
      <div class="swatch-row" style="top:46px">
        <div class="swatch swatch--grass" role="img" aria-label="Native grasses"></div>
        <div class="swatch swatch--lomandra" role="img" aria-label="Lomandra"></div>
        <div class="swatch swatch--lillypilly" role="img" aria-label="Lillypilly hedge foliage"></div>
      </div>
    </section>

    <footer>
      <div class="footer-brand"><span class="brand-dot"></span>Fernwick Plotcraft</div>
      <div class="footer-kit">Tropical Shade Garden Kit</div>
      <svg class="corner-frame" width="80" height="66" viewBox="0 0 80 66" aria-hidden="true">
        <polyline points="3,66 18,5 80,18" fill="none" stroke="#8dc63f" stroke-width="5"/>
      </svg>
      <span class="page-number">4</span>
    </footer>
  </main>
</body>
</html>
```